Web Design for Employee Benefits / Corporate Insurance Solutions Firm - Using Divi (by Corvane Pix...

*Please use Divi from corvane pixels to create the design.

Company Name: Harbourline By Tomas(Logo attached)

Colour scheme: White / Teal / Aquamarine / Grey

We are a firm that provides the following solutions for businesses:
- employee medical benefits
- office insurance
- talent retention / long-service retirement solutions
- keyman insurance

We need a website to provide information about our services, as well as password portals for employees of each company that we take care of.

Portals would provide specific information for employees of each company:
- employee handbook
- plan benefits & references
- claim forms

The site would also list articles for Human Resource Professionals and give them information about latest updates in the employee benefits / corporate culture best practices.

Human Resource Executives, Managing Directors, Chief Finance Officers, Employees

Business Consultant

• Should be able to adjust the website widths & font sizes to be viewed on:
• - computer;
• - slatu;
• - smartphone

```html
<!DOCTYPE html>
<html lang="en">
<head>
<meta charset="utf-8">
<title>Harbourline By Tomas</title>
<link href="https://fonts.googleapis.com/css2?family=Lato:ital,wght@0,300;0,400;0,700;1,400&display=swap" rel="stylesheet">
<style>
:root{
  --green:#45c57f;
  --green-dark:#33a866;
  --ink:#2b2b2b;
  --grey:#6f6f6f;
  --light:#e9e9e9;
  --footer:#d6d6d6;
  --white:#ffffff;
  --nav:rgba(20,24,26,.8);
}
*{box-sizing:border-box;margin:0;padding:0}
html,body{width:1200px;height:3884px;overflow:hidden}
body{font-family:'Lato',sans-serif;color:var(--ink);background:var(--white);position:relative}

.hero{position:absolute;top:0;left:0;width:1200px;height:732px;overflow:hidden}
.hero-photo{position:absolute;inset:0;background:
  radial-gradient(ellipse 260px 200px at 160px 300px,rgba(214,190,170,.75),transparent),
  radial-gradient(ellipse 300px 220px at 1010px 340px,rgba(225,215,205,.7),transparent),
  radial-gradient(ellipse 420px 180px at 620px 640px,rgba(190,170,150,.55),transparent),
  radial-gradient(ellipse 240px 160px at 880px 120px,rgba(170,120,90,.6),transparent),
  linear-gradient(160deg,#5b5f63 0%,#7a6d60 45%,#4a4f54 100%)}
.hero-shade{position:absolute;inset:0;background:rgba(15,18,20,.45)}
.nav{position:absolute;top:0;left:0;width:1200px;height:48px;background:var(--nav);display:flex;justify-content:center;align-items:center;gap:34px}
.nav a{color:var(--white);text-decoration:none;font-size:15px;letter-spacing:.5px;text-transform:uppercase}
.nav a.active{color:var(--green)}
.brand{position:absolute;top:118px;left:0;width:1200px;text-align:center;color:var(--white)}
.brand-mark{width:124px;height:124px;border-radius:50%;background:var(--green);margin:0 auto 18px}
.brand-name{font-size:40px;letter-spacing:6px;font-weight:400;text-transform:uppercase}
.hero-title{position:absolute;top:366px;width:1200px;text-align:center;color:var(--white);font-size:38px;font-weight:700;text-transform:uppercase}
.hero-actions{position:absolute;top:432px;width:1200px;display:flex;justify-content:center;gap:22px}
.btn{display:inline-block;height:44px;line-height:40px;padding:0 30px;font-size:15px;text-transform:uppercase;text-decoration:none;border:2px solid var(--green)}
.btn-outline{color:var(--green);background:rgba(0,0,0,.35)}
.btn-solid{color:var(--white);background:var(--green)}
.scroll-down{position:absolute;top:648px;left:580px;width:40px;height:40px;border-radius:50%;border:2px solid var(--white)}

.services{position:absolute;top:770px;left:180px;width:840px;display:flex;justify-content:space-between}
.service{width:190px;text-align:center}
.service svg{width:60px;height:60px}
.service h3{color:var(--green);font-size:19px;font-weight:400;margin-top:8px}
.service .sub{color:var(--green);font-size:13px}
.service p{font-size:13px;color:var(--grey);line-height:1.5;margin-top:10px}
.section-title{text-align:center;font-size:36px;font-weight:700;text-transform:uppercase}

.articles{position:absolute;top:1066px;left:0;width:1200px}
.article-grid{display:flex;justify-content:center;gap:14px;margin-top:32px}
.article-photo{width:210px;height:152px}
.ph-a1{background:radial-gradient(ellipse 70px 60px at 60px 70px,#e2d6c8,transparent),linear-gradient(135deg,#9aa3ab,#4b5158)}
.ph-a2{background:radial-gradient(ellipse 80px 50px at 130px 90px,#d9dde0,transparent),linear-gradient(135deg,#c8c2b8,#5d5a56)}
.ph-a3{background:radial-gradient(ellipse 60px 70px at 100px 80px,#c6b09a,transparent),linear-gradient(135deg,#3f3a36,#8a7e72)}
.ph-a4{background:radial-gradient(ellipse 80px 60px at 110px 70px,#ebe3da,transparent),linear-gradient(135deg,#c9b8a6,#7a8690)}
.articles .btn-solid{display:block;width:166px;margin:40px auto 0;text-align:center}

.team{position:absolute;top:1445px;left:0;width:1200px;height:571px;background:var(--green);color:var(--white)}
.team .section-title{margin-top:58px}
.team-intro{width:720px;margin:20px auto 0;text-align:center;font-size:13px;line-height:1.55}
.members{display:flex;justify-content:center;gap:50px;margin-top:40px}
.member{width:176px;text-align:center}
.member-photo{width:176px;height:176px;border-radius:50%;border:4px solid var(--white)}
.ph-m1{background:radial-gradient(circle at 50% 40%,#b58a6e 0 28%,transparent 30%),linear-gradient(180deg,#7a6a5c 0%,#3a3633 100%)}
.ph-m2{background:radial-gradient(circle at 50% 40%,#d8a98a 0 28%,transparent 30%),linear-gradient(180deg,#f2f2f2 0%,#d37f6c 100%)}
.ph-m3{background:radial-gradient(circle at 50% 42%,#e0b090 0 30%,transparent 32%),linear-gradient(180deg,#6aa63a 0%,#3f7a2a 100%)}
.ph-m4{background:radial-gradient(circle at 50% 40%,#d9b096 0 28%,transparent 30%),linear-gradient(180deg,#f0f0f0 0%,#39424d 100%)}
.member h4{font-size:15px;font-weight:700;margin-top:14px;text-transform:uppercase}
.member span{font-size:13px}

.gallery{position:absolute;top:2016px;left:0;width:1200px;height:691px;background:var(--white)}
.gallery-main{position:absolute;left:0;top:0;width:604px;height:691px;background:
  radial-gradient(ellipse 150px 170px at 130px 230px,#eee8e2,transparent),
  radial-gradient(ellipse 170px 190px at 390px 250px,#d9c2aa,transparent),
  radial-gradient(ellipse 230px 140px at 330px 560px,#8f7d68,transparent),
  linear-gradient(135deg,#c9c2ba,#6f6458)}
.gallery-top{position:absolute;left:608px;top:0;width:592px;height:330px;background:
  radial-gradient(ellipse 90px 150px at 230px 190px,#2b2e33,transparent),
  radial-gradient(ellipse 120px 130px at 480px 180px,#e6e0da,transparent),
  linear-gradient(135deg,#f1efec,#8b8e92)}
.gallery-bottom{position:absolute;left:608px;top:334px;width:592px;height:357px;background:
  radial-gradient(ellipse 140px 170px at 120px 240px,#2e3033,transparent),
  radial-gradient(ellipse 130px 150px at 400px 180px,#ddd6ce,transparent),
  linear-gradient(135deg,#b3a493,#4b4d50)}

.testimonials{position:absolute;top:2707px;left:0;width:1200px;height:424px;background:var(--green);color:var(--white);text-align:center}
.testimonials .section-title{margin-top:68px}
.quote{width:720px;margin:24px auto 0;font-size:17px;font-style:italic;line-height:1.5}
.author{font-size:22px;margin-top:30px}
.dots{display:flex;justify-content:center;gap:8px;margin-top:24px}
.dots i{width:12px;height:12px;border-radius:50%;background:var(--white)}
.dots i.off{background:transparent;border:2px solid var(--white)}
.arrow{position:absolute;top:172px;width:30px;height:30px}
.arrow.left{left:76px}.arrow.right{right:76px}

.contact{position:absolute;top:3131px;left:0;width:1200px;height:689px}
.contact .section-title{margin-top:62px}
.contact-intro{width:560px;margin:14px auto 0;text-align:center;font-size:14px;color:var(--grey);line-height:1.5}
.contact-form{position:absolute;top:220px;left:188px;width:840px}
.field{background:var(--light);height:48px;font-size:14px;color:var(--grey);padding:14px 16px}
.row{display:flex;gap:20px}
.row .field{width:410px}
.field.message{height:136px;margin-top:12px}
.submit{position:absolute;right:0;top:212px;width:156px;height:44px;border:2px solid var(--green);color:var(--green);text-align:center;line-height:40px;font-size:14px;text-transform:uppercase}
.footer{position:absolute;top:3820px;left:0;width:1200px;height:64px;background:var(--footer);text-align:center;line-height:64px;font-size:13px;color:var(--grey)}
</style>
</head>
<body>
<header class="hero">
  <div class="hero-photo" role="img" aria-label="Business team meeting around a table"></div>
  <div class="hero-shade"></div>
  <nav class="nav">
    <a href="#" class="active">Home</a><a href="#">About Us</a><a href="#">Services</a><a href="#">Articles</a><a href="#">Contact</a><a href="#">Member Login</a>
  </nav>
  <div class="brand">
    <div class="brand-mark"></div>
    <div class="brand-name">Harbourline By Tomas</div>
  </div>
  <h1 class="hero-title">Welcome to our website</h1>
  <div class="hero-actions"><a class="btn btn-outline" href="#">View Services</a><a class="btn btn-solid" href="#">Contact Us</a></div>
  <div class="scroll-down"><svg viewBox="0 0 40 40" width="36" height="36"><path d="M12 15 L18 22 L24 15" fill="none" stroke="#fff" stroke-width="2"/></svg></div>
</header>

<section class="services">
  <div class="service">
    <svg viewBox="0 0 60 60"><g fill="none" stroke="#45c57f" stroke-width="2.5"><rect x="22" y="6" width="16" height="12"/><rect x="6" y="40" width="14" height="12"/><rect x="40" y="40" width="14" height="12"/><path d="M30 18v10M13 40V28h34v12"/></g></svg>
    <h3>Review</h3><div class="sub">Existing Clients Data</div>
    <p>Would you like to know the utilization experience of your company's employee benefits?</p>
  </div>
  <div class="service">
    <svg viewBox="0 0 60 60"><g fill="none" stroke="#45c57f" stroke-width="2.5"><circle cx="30" cy="16" r="9"/><path d="M12 54c0-12 8-20 18-20s18 8 18 20z"/><path d="M26 34l4 8 4-8"/></g></svg>
    <h3>Consultation</h3><div class="sub">For existing clients only</div>
    <p>Do you need help with your claims process or client outcomes? Do you need advice on questions with your personal portfolio?</p>
  </div>
  <div class="service">
    <svg viewBox="0 0 60 60"><g fill="none" stroke="#45c57f" stroke-width="2.5"><path d="M30 8c-12 0-20 9-20 19 0 7 4 11 8 14v9h24v-9c4-3 8-7 8-14 0-10-8-19-20-19z"/><path d="M24 50v4h12v-4"/></g></svg>
    <h3>Draft A New Solution</h3>
    <p>Are you a new startup wishing to retain your talent pool with medical benefits?</p>
  </div>
  <div class="service">
    <svg viewBox="0 0 60 60"><g fill="none" stroke="#45c57f" stroke-width="2.5"><circle cx="30" cy="14" r="7"/><path d="M30 21v20M18 30h24M30 41l-10 13M30 41l10 13"/></g></svg>
    <h3>Review &amp; Assess</h3>
    <p>Would you like an unbiased opinion of your current employee benefits program?</p>
  </div>
</section>

<section class="articles">
  <h2 class="section-title">Recent Articles</h2>
  <div class="article-grid">
    <div class="article-photo ph-a1" role="img" aria-label="Colleagues reviewing documents"></div>
    <div class="article-photo ph-a2" role="img" aria-label="Team working at laptops"></div>
    <div class="article-photo ph-a3" role="img" aria-label="Business handshake"></div>
    <div class="article-photo ph-a4" role="img" aria-label="Senior couple with adviser"></div>
  </div>
  <a class="btn btn-solid" href="#">View All</a>
</section>

<section class="team">
  <h2 class="section-title">Our Team</h2>
  <p class="team-intro">Lorem ipsum dolor sit amet, consectetur adipiscing elit. Integer posuere erat a ante venenatis dapibus posuere velit aliquet. Cras justo odio, dapibus ac facilisis in, egestas eget quam. Cum sociis natoque penatibus et magnis dis parturient montes, nascetur ridiculus mus. Maecenas faucibus mollis interdum.</p>
  <div class="members">
    <div class="member"><div class="member-photo ph-m1" role="img" aria-label="Portrait of team member"></div><h4>Member Name</h4><span>Post Designation</span></div>
    <div class="member"><div class="member-photo ph-m2" role="img" aria-label="Portrait of team member"></div><h4>Member Name</h4><span>Post Designation</span></div>
    <div class="member"><div class="member-photo ph-m3" role="img" aria-label="Portrait of team member"></div><h4>Member Name</h4><span>Post Designation</span></div>
    <div class="member"><div class="member-photo ph-m4" role="img" aria-label="Portrait of team member"></div><h4>Member Name</h4><span>Post Designation</span></div>
  </div>
</section>

<section class="gallery">
  <div class="gallery-main" role="img" aria-label="Senior couple meeting a financial adviser"></div>
  <div class="gallery-top" role="img" aria-label="Business people shaking hands in an office"></div>
  <div class="gallery-bottom" role="img" aria-label="Colleagues in a meeting room"></div>
</section>

<section class="testimonials">
  <h2 class="section-title">Testimonials</h2>
  <p class="quote">“Lorem ipsum dolor sit amet, consectetur adipiscing elit. Integer posuere erat a ante venenatis dapibus posuere velit aliquet. Cras justo odio, dapibus ac facilisis in, egestas eget quam. Cum sociis natoque penatibus et magnis.”</p>
  <div class="author">By Author Name</div>
  <div class="dots"><i class="off"></i><i></i><i></i><i></i></div>
  <svg class="arrow left" viewBox="0 0 30 30"><path d="M20 4 L9 15 L20 26" fill="none" stroke="#fff" stroke-width="3"/></svg>
  <svg class="arrow right" viewBox="0 0 30 30"><path d="M10 4 L21 15 L10 26" fill="none" stroke="#fff" stroke-width="3"/></svg>
</section>

<section class="contact">
  <h2 class="section-title">Contact Us</h2>
  <p class="contact-intro">Vestibulum ante ipsum primis in faucibus orci luctus et ultrices posuere cubilia curae. Curabitur blandit tempus porttitor.</p>
  <div class="contact-form">
    <div class="row"><div class="field">Name</div><div class="field">Email address</div></div>
    <div class="field message">Message</div>
    <div class="submit">Submit</div>
  </div>
</section>

<footer class="footer">© 2018 Company Name. All rights reserved. Terms of Use</footer>
</body>
</html>
```